Bauzaun-Banner für Abbruchfirma und Schadstoffsanierung
Zielgruppe
Abbruchfirma und Schadstoffsanierung
Aufgabenstellung
Unsere Logo und die Tätigkeiten die wir anbieten müssen vertreten sein
Wir möchten einen Banner für einen Bauzaun entwickeln lassen. Maße sind 340cm x 173 cm

```html
<!DOCTYPE html>
<html lang="de">
<head>
<meta charset="utf-8">
<title>Bauzaun-Banner – Talbrück Bauservice</title>
<link rel="stylesheet" href="https://fonts.googleapis.com/css2?family=Jost:wght@500;700&family=Signika:wght@600&display=swap">
<style>
  :root {
    --page: #d9dadc;
    --panel: #efeeec;
    --red: #cc2323;
    --ink: #141414;
    --white: #ffffff;
    --photo-dark: #2b2626;
    --photo-mid: #6e605c;
    --photo-light: #b7a9a2;
  }
  html, body {
    margin: 0;
    width: 1200px;
    height: 800px;
    overflow: hidden;
    background: var(--page);
  }
  .banner {
    position: absolute;
    left: 20px;
    top: 105px;
    width: 1160px;
    height: 590px;
    overflow: hidden;
    background: var(--photo-dark);
    box-shadow: 0 6px 24px rgba(0,0,0,.25);
  }
  .banner-shapes {
    position: absolute;
    inset: 0;
  }
  .brand {
    position: absolute;
    left: 50px;
    top: 90px;
    width: 380px;
  }
  .brand-row {
    display: flex;
    align-items: center;
    gap: 14px;
  }
  .brand-square {
    width: 54px;
    height: 54px;
    background: var(--red);
    flex: none;
  }
  .brand-name {
    font-family: "Jost", sans-serif;
    font-weight: 500;
    font-size: 34px;
    line-height: 1;
    color: var(--ink);
    text-transform: uppercase;
    letter-spacing: .5px;
  }
  .brand-services {
    margin-top: 12px;
    font-family: "Jost", sans-serif;
    font-weight: 500;
    font-size: 12px;
    letter-spacing: 1.6px;
    color: var(--ink);
    text-transform: uppercase;
  }
  .headline {
    position: absolute;
    left: 50px;
    top: 300px;
    margin: 0;
    font-family: "Jost", sans-serif;
    font-weight: 700;
    font-size: 60px;
    line-height: 1.1;
    color: var(--ink);
  }
  .headline-highlight {
    background: var(--red);
    color: var(--white);
    padding: 0 8px;
  }
  .website {
    position: absolute;
    left: 50px;
    bottom: 45px;
    font-family: "Jost", sans-serif;
    font-weight: 700;
    font-size: 22px;
    color: var(--ink);
  }
  .services {
    position: absolute;
    right: 30px;
    top: 0;
    margin: 0;
    padding: 0;
    list-style: none;
    font-family: "Signika", sans-serif;
    font-weight: 600;
    color: var(--white);
    text-align: right;
  }
  .service {
    position: absolute;
    right: 0;
    white-space: nowrap;
    font-size: 34px;
    line-height: 1.05;
  }
  .service-1 { top: 28px; }
  .service-2 { top: 88px; }
  .service-3 { top: 148px; }
  .service-4 { top: 212px; }
</style>
</head>
<body>
<main class="banner">
  <svg class="banner-shapes" viewBox="0 0 1160 590" width="1160" height="590">
    <defs>
      <linearGradient id="photoTone" x1="0" y1="0" x2="1" y2="1">
        <stop offset="0" stop-color="var(--photo-mid)"/>
        <stop offset=".45" stop-color="var(--photo-dark)"/>
        <stop offset=".75" stop-color="var(--photo-light)"/>
        <stop offset="1" stop-color="var(--photo-mid)"/>
      </linearGradient>
    </defs>
    <rect class="photo-area" x="0" y="0" width="1160" height="590" fill="url(#photoTone)" role="img" aria-label="Foto: Arbeiter schlägt mit einem Vorschlaghammer eine Ziegelwand ein, Staub und Trümmer fliegen"/>
    <path class="text-panel" d="M0 0 H470 Q530 0 515 90 L385 590 H0 Z" fill="var(--panel)"/>
    <g class="service-bands" fill="var(--red)">
      <polygon points="740,30 1160,10 1160,70 715,85"/>
      <polygon points="710,90 1160,72 1160,132 685,148"/>
      <polygon points="680,154 1160,136 1160,196 655,212"/>
      <polygon points="650,218 1160,198 1160,292 620,310"/>
    </g>
  </svg>

  <div class="brand">
    <div class="brand-row">
      <span class="brand-square"></span>
      <span class="brand-name">Talbrück Bauservice</span>
    </div>
    <div class="brand-services">Schadstoffsanierung | Abbruch | Entsorgung</div>
  </div>

  <h1 class="headline">Wir machen<br><span class="headline-highlight">PLATZ</span> für<br>Neues!</h1>

  <div class="website">www.talbrueck-bau.de</div>

  <ul class="services">
    <li class="service service-1">Industrierückbau</li>
    <li class="service service-2">Abbruch &amp; Entkernen</li>
    <li class="service service-3">Entsorgung</li>
    <li class="service service-4">Schadstoffsanierung<br>Asbest, KMF, PAK</li>
  </ul>
</main>
</body>
</html>
```